Business Card Design Project

Basic business card with minimal details. I just need company name, email & web address, telephone and my name.
I would like the back of the card to be grey with my logo & company name centred.

Target Market(s)

Architects
Builders
Property Developers

Industry/Entity Type

Business

Font styles to use
Sans Serif

Colors

Designer to choose colors to be used in the design.

Requirements
Must have
• Framewise Build
Marcus Helby - Director
M: 0427 593184
E: marcus@framewisebuild.com.au
W: www.framewisebuild.com.au
Should not have
• No other images or pictures

```html
<!DOCTYPE html>
<html lang="en">
<head>
<meta charset="utf-8">
<title>Framewise Build – Business Card</title>
<link rel="stylesheet" href="https://fonts.googleapis.com/css2?family=Source+Sans+3:ital,wght@0,400;0,600;0,700;1,400&display=swap">
<style>
  :root {
    --stage: #000000;
    --card: #c3c4c6;
    --slate: #4f6373;
    --crimson: #b2122f;
    --ink: #1b1b1d;
    --ink-soft: #2e2e31;
    --label: #e6e6e6;
  }
  * { box-sizing: border-box; margin: 0; padding: 0; }
  html, body {
    width: 1200px;
    height: 1134px;
    overflow: hidden;
    background: var(--stage);
    font-family: "Source Sans 3", sans-serif;
  }
  .spread {
    position: absolute;
    top: 382px;
    left: 40px;
    width: 1120px;
    display: flex;
    justify-content: space-between;
  }
  .side { width: 540px; }
  .card {
    position: relative;
    width: 540px;
    height: 300px;
    background: var(--card);
  }
  .side-label {
    margin-top: 22px;
    text-align: center;
    color: var(--label);
    font-style: italic;
    font-size: 23px;
  }

  /* back of card */
  .card-back {
    display: flex;
    flex-direction: column;
    align-items: center;
    justify-content: center;
    gap: 26px;
  }
  .brand-square {
    width: 70px;
    height: 70px;
    background: var(--crimson);
  }
  .brand-name {
    color: var(--slate);
    font-weight: 600;
    font-size: 40px;
    letter-spacing: 3px;
    text-transform: uppercase;
    line-height: 1;
  }

  /* front of card */
  .card-front .header {
    position: absolute;
    top: 34px;
    right: 16px;
    text-align: left;
  }
  .card-front .brand-name {
    font-size: 37px;
    letter-spacing: 2px;
  }
  .holder {
    margin-top: 4px;
    font-size: 21px;
    line-height: 1;
  }
  .holder-name { color: var(--crimson); font-weight: 700; }
  .holder-role { color: var(--slate); }
  .contacts {
    position: absolute;
    right: 16px;
    bottom: 36px;
    list-style: none;
    text-align: right;
    font-size: 18px;
    line-height: 27px;
  }
  .contact-key { color: var(--ink-soft); font-style: italic; font-weight: 400; }
  .contact-value { color: var(--ink); font-weight: 700; }
</style>
</head>
<body>
  <main class="spread">
    <section class="side">
      <div class="card card-back">
        <span class="brand-square" aria-hidden="true"></span>
        <span class="brand-name">Framewise Build</span>
      </div>
      <p class="side-label">back side</p>
    </section>

    <section class="side">
      <div class="card card-front">
        <header class="header">
          <h1 class="brand-name">Framewise Build</h1>
          <p class="holder"><span class="holder-name">Marcus Helby</span> <span class="holder-role">Director</span></p>
        </header>
        <ul class="contacts">
          <li><span class="contact-key">phone number</span> <span class="contact-value">0427 593184</span></li>
          <li><span class="contact-key">email</span> <span class="contact-value">marcus@framewisebuild.com.au</span></li>
          <li><span class="contact-key">website</span> <span class="contact-value">www.framewisebuild.com.au</span></li>
        </ul>
      </div>
      <p class="side-label">front side</p>
    </section>
  </main>
</body>
</html>
```